Business Card Design

After a corporate career in the finance sector I am now operating on my own as a consultant. I require a simple design, and want a strong card which is targeted at a conservative audience.

Target Market(s)

highly educated senior management, directors of companies, finance sector

Industry/Entity Type

Conservative

Contact Information for Business Card

Ruth Danver
Consultant
Mobile: 0417 862 450
Email: ruth.danv@mailcove.net

Requirements
Should not have
• I don't want the colours green/yellow/brown

```html
<!DOCTYPE html>
<html lang="en">
<head>
<meta charset="utf-8">
<title>Ruth Danver — Business Card</title>
<link rel="stylesheet" href="https://fonts.googleapis.com/css2?family=Domine:wght@700&display=swap">
<style>
  :root {
    --page-bg: #e9e9ec;
    --metal-light: #e4e5e7;
    --metal-mid: #c3c5c8;
    --metal-dark: #a9abae;
    --ink-black: #050505;
    --gloss: #8a8c90;
    --name-ink: #111111;
    --contact-ink: #f2f2f2;
  }
  * { margin: 0; padding: 0; box-sizing: border-box; }
  html, body {
    width: 1200px;
    height: 900px;
    overflow: hidden;
    background: var(--page-bg);
  }
  .business-card {
    position: absolute;
    left: 180px;
    top: 210px;
    width: 840px;
    height: 480px;
    border-radius: 30px;
    overflow: hidden;
    background:
      repeating-linear-gradient(0deg, rgba(255,255,255,0.18) 0 1px, rgba(0,0,0,0.05) 1px 2px, rgba(255,255,255,0) 2px 3px),
      linear-gradient(160deg, var(--metal-light) 0%, var(--metal-mid) 55%, var(--metal-dark) 100%);
    box-shadow: 0 10px 30px rgba(0,0,0,0.25);
    font-family: "Domine", Georgia, serif;
  }
  .card-shapes {
    position: absolute;
    inset: 0;
    width: 100%;
    height: 100%;
  }
  .identity {
    position: absolute;
    left: 84px;
    top: 150px;
    display: inline-flex;
    flex-direction: column;
    align-items: flex-end;
    color: var(--name-ink);
  }
  .identity__name {
    font-size: 50px;
    line-height: 1;
    font-weight: 700;
    letter-spacing: 0.5px;
  }
  .identity__role {
    font-size: 17px;
    font-weight: 700;
    line-height: 1;
    margin-top: 2px;
    letter-spacing: 0.5px;
  }
  .contact-list {
    position: absolute;
    left: 478px;
    top: 286px;
    list-style: none;
    color: var(--contact-ink);
  }
  .contact-list__item {
    display: flex;
    align-items: center;
    gap: 22px;
    font-size: 22px;
    font-weight: 700;
    letter-spacing: 0.8px;
    line-height: 1;
    margin-bottom: 22px;
  }
  .contact-list__icon {
    width: 20px;
    height: 20px;
    flex: none;
  }
</style>
</head>
<body>
  <div class="business-card">
    <svg class="card-shapes" viewBox="0 0 840 480" preserveAspectRatio="none" aria-hidden="true">
      <path d="M680 0 C620 230 330 330 0 400 L0 480 L840 480 L840 0 Z" fill="var(--ink-black)"/>
      <path d="M680 0 C620 230 330 330 0 400" fill="none" stroke="var(--gloss)" stroke-width="3" opacity="0.7"/>
    </svg>

    <div class="identity">
      <h1 class="identity__name">Ruth Danver</h1>
      <p class="identity__role">consultant</p>
    </div>

    <ul class="contact-list">
      <li class="contact-list__item">
        <svg class="contact-list__icon" viewBox="0 0 20 20" aria-label="Mobile">
          <rect x="5.5" y="2" width="9" height="16" rx="1.5" fill="none" stroke="var(--contact-ink)" stroke-width="1.6"/>
          <circle cx="10" cy="15" r="1" fill="var(--contact-ink)"/>
        </svg>
        <span>0417 862 450</span>
      </li>
      <li class="contact-list__item">
        <svg class="contact-list__icon" viewBox="0 0 20 20" aria-label="Email">
          <rect x="1.5" y="4.5" width="17" height="11" fill="none" stroke="var(--contact-ink)" stroke-width="1.6"/>
          <path d="M1.5 4.5 L10 11 L18.5 4.5" fill="none" stroke="var(--contact-ink)" stroke-width="1.6"/>
        </svg>
        <span>ruth.danv@mailcove.net</span>
      </li>
    </ul>
  </div>
</body>
</html>
```